Saffron Table signage

Simple design for a new food court outlet: Saffron Table
They serve a fusion of Indian and Mediterranean food and we need signage with fonts and colors that reflect the warmth and spice of the cultures.
The sign is long and skinny. 1 foot tall by 18 feet long.

Target Market(s)

Ski resort guests eating at our base area food court with multiple selections to choose from.

Industry/Entity Type

Court

Requirements
Must have
• Clear readability. Name should be prominent and bright.
Nice to have
• Simple clear text. Possibly use fonts that relate to Indian and Mediterranean inspirations. Warm colors that make you want to eat the food.
Should not have
• Should not have too many graphic elements that it makes it hard to read.

```html
<!DOCTYPE html>
<html lang="en">
<head>
<meta charset="utf-8">
<title>Saffron Table – Signage</title>
<link rel="stylesheet" href="https://fonts.googleapis.com/css2?family=Kaushan+Script&family=Baloo+2:wght@600&display=swap">
<style>
  :root {
    --red: #e60c16;
    --orange: #ff5a12;
    --deep-red: #c4060e;
    --leaf: #57d62a;
    --leaf-dark: #2f9e12;
    --cream: #fff8b8;
    --butter: #fbe27a;
    --ink: #111;
    --white: #fff;
    --page: #fff;
  }
  * { margin: 0; padding: 0; box-sizing: border-box; }
  html, body {
    width: 1200px; height: 811px; overflow: hidden;
    background: var(--page);
  }
  .canvas { position: relative; width: 1200px; height: 811px; }
  .sign {
    position: absolute; left: 59px; width: 1080px;
    background: linear-gradient(180deg, var(--red) 0%, #f22a12 50%, var(--orange) 100%);
    overflow: hidden;
  }
  .sign--slim { top: 144px; height: 63px; }
  .sign--full { top: 315px; height: 126px; }
  .sign--tagline { top: 536px; height: 126px; }
  .sign__frame { position: absolute; inset: 0; width: 100%; height: 100%; }
  .flourish-area {
    position: absolute; left: 0; top: 0; height: 100%;
    background: radial-gradient(ellipse at 45% 55%, rgba(190,10,20,0.45), rgba(230,20,20,0) 70%);
  }
  .sign--slim .flourish-area { width: 148px; }
  .sign--full .flourish-area { width: 312px; }
  .brand-name {
    position: absolute; top: 0; height: 100%;
    display: flex; align-items: center; justify-content: center;
    font-family: "Kaushan Script", cursive;
    color: var(--ink); white-space: nowrap;
  }
  .sign--slim .brand-name { left: 175px; width: 279px; font-size: 33px; }
  .sign--full .brand-name { left: 382px; width: 575px; font-size: 70px; }
  .tagline {
    position: absolute; font-family: "Baloo 2", sans-serif; font-weight: 600;
    color: var(--white); white-space: nowrap;
  }
  .sign--slim .tagline { left: 596px; top: 0; height: 63px; line-height: 63px; font-size: 22px; }
  .sign--tagline .tagline {
    left: 80px; top: 0; height: 126px; line-height: 128px; font-size: 44px;
    text-shadow: 3px 4px 5px rgba(90,0,0,0.55);
  }
</style>
</head>
<body>
<main class="canvas">

  <section class="sign sign--slim">
    <svg class="sign__frame" viewBox="0 0 1080 63" preserveAspectRatio="none" aria-hidden="true">
      <defs>
        <radialGradient id="plaque-slim" cx="50%" cy="45%" r="65%">
          <stop offset="0" stop-color="var(--cream)"/>
          <stop offset="1" stop-color="var(--butter)"/>
        </radialGradient>
      </defs>
      <path d="M146,0 H160 V63 H146 Q152,46 144,32 Q152,16 146,0 Z" fill="var(--leaf)"/>
      <path d="M160,0 H176 V63 H160 Q167,46 159,32 Q167,16 160,0 Z" fill="var(--deep-red)"/>
      <path d="M454,0 H470 Q463,16 471,32 Q463,46 470,63 H454 Z" fill="var(--deep-red)"/>
      <path d="M470,0 H482 Q475,16 483,32 Q475,46 482,63 H470 Z" fill="var(--leaf)"/>
      <path d="M182,2 H448 Q444,12 456,16 V47 Q444,51 448,61 H182 Q186,51 174,47 V16 Q186,12 182,2 Z" fill="url(#plaque-slim)"/>
    </svg>
    <div class="flourish-area" role="img" aria-label="Red swirling knot flourish ornament"></div>
    <h1 class="brand-name">Saffron Table</h1>
    <p class="tagline">Mediterranean &amp; Indian Fusion</p>
  </section>

  <section class="sign sign--full">
    <svg class="sign__frame" viewBox="0 0 1080 126" preserveAspectRatio="none" aria-hidden="true">
      <defs>
        <radialGradient id="plaque-full" cx="50%" cy="45%" r="65%">
          <stop offset="0" stop-color="var(--cream)"/>
          <stop offset="1" stop-color="var(--butter)"/>
        </radialGradient>
      </defs>
      <path d="M312,0 H338 V126 H312 Q324,94 308,63 Q324,32 312,0 Z" fill="var(--leaf)"/>
      <path d="M338,0 H384 V126 H338 Q350,94 334,63 Q350,32 338,0 Z" fill="var(--deep-red)"/>
      <path d="M955,0 H1000 Q988,32 1004,63 Q988,94 1000,126 H955 Z" fill="var(--deep-red)"/>
      <path d="M1000,0 H1022 Q1010,32 1026,63 Q1010,94 1022,126 H1000 Z" fill="var(--leaf)"/>
      <path d="M396,3 H944 Q937,22 958,30 V96 Q937,104 944,123 H396 Q403,104 382,96 V30 Q403,22 396,3 Z" fill="url(#plaque-full)"/>
    </svg>
    <div class="flourish-area" role="img" aria-label="Large red swirling knot flourish ornament"></div>
    <h2 class="brand-name">Saffron Table</h2>
  </section>

  <section class="sign sign--tagline">
    <p class="tagline">Mediterranean &amp; Indian Fusion</p>
  </section>

</main>
</body>
</html>
```